Corvel's Auto Detailing is the company name. I will upload a picture that is something similar. However a few things will be different. I want my company name to be on it. And a picture of a nice car. As well as the packages offered. Also phone number which is 5047162283. Call or text. As far as the packages goes, I want the exact layout of the picture I uploaded. The only difference would be the prices. For full detail the price should be $149.99, engine detail is $39.99 headlight restoration is $19.99 exterior wash is $59.99 Interior is $59.99. Please make it pretty. I would like to see a copy before printing

```html
<!DOCTYPE html>
<html lang="en">
<head>
<meta charset="utf-8">
<title>Corvel's Auto Detailing – Services</title>
<link href="https://fonts.googleapis.com/css2?family=Archivo+Black&family=Roboto+Condensed:wght@700&family=Roboto:ital,wght@0,700;1,700&display=swap" rel="stylesheet">
<style>
  :root{
    --navy-panel:rgba(34,46,140,.94);
    --blue-panel:#1460ab;
    --blue-panel-2:#1566b3;
    --yellow:#ffef1a;
    --white:#ffffff;
    --red:#e4151f;
  }
  *{box-sizing:border-box;margin:0;padding:0}
  html,body{width:800px;height:1200px;overflow:hidden;background:var(--white)}
  .flyer{
    position:relative;width:800px;height:1200px;overflow:hidden;
    background:linear-gradient(180deg,#5fb2e6 0%,#3d98d8 40%,#6dbbea 70%,#a9daf5 100%);
    font-family:"Roboto Condensed",sans-serif;font-weight:700;
  }
  .water-texture{
    position:absolute;inset:0;
    background:
      radial-gradient(ellipse at 10% 60%,rgba(255,255,255,.55),transparent 40%),
      radial-gradient(ellipse at 5% 95%,rgba(255,255,255,.6),transparent 35%),
      radial-gradient(ellipse at 90% 85%,rgba(255,255,255,.35),transparent 40%);
  }
  .car-photo{
    position:absolute;left:390px;top:0;width:410px;height:380px;
    background:radial-gradient(ellipse at 60% 40%,#3a6fe0 0%,#1b3fae 45%,#0e2468 75%,rgba(60,140,210,0) 100%);
  }
  .brand{position:absolute;left:30px;top:10px;width:380px}
  .brand-name{
    font-family:"Roboto Condensed",sans-serif;font-weight:700;
    color:var(--yellow);font-size:50px;line-height:50px;text-transform:uppercase;letter-spacing:1px;
  }
  .brand-phone{
    margin-top:6px;font-size:36px;line-height:38px;color:var(--white);letter-spacing:1px;
  }
  .panel{position:absolute}
  .panel-title{
    font-family:"Archivo Black",sans-serif;font-weight:400;text-transform:uppercase;
    color:var(--yellow);font-size:42px;line-height:44px;letter-spacing:1px;
    transform:skewX(-10deg);transform-origin:left bottom;
  }
  .service-list{list-style:none;color:var(--white);font-size:21.5px;line-height:23.7px;text-transform:uppercase;font-weight:700}
  .price-tag{
    position:absolute;background:var(--white);border:3px solid var(--red);
    color:var(--red);text-align:center;font-family:"Roboto",sans-serif;font-weight:700;
  }
  .price-tag .from{font-style:italic;font-size:11px;line-height:13px;margin-top:4px;display:block}
  .price-tag .amount{font-size:41px;line-height:40px;display:block;letter-spacing:-.5px}
  .price-tag .tax{font-size:10px;line-height:10px;color:#c0141b;display:block}

  .full{left:11px;top:158px;width:599px;height:378px;background:var(--navy-panel);padding:14px 0 0 24px}
  .full .service-list{margin-top:12px}
  .full .price-tag{left:427px;top:284px;width:158px;height:70px}

  .exterior{left:171px;top:544px;width:601px;height:258px;background:var(--blue-panel);padding:12px 0 0 16px}
  .exterior .service-list{margin-top:12px;padding-left:8px}
  .exterior .price-tag{left:427px;top:106px;width:158px;height:70px}

  .interior{left:20px;top:810px;width:600px;height:216px;background:var(--blue-panel-2);padding:16px 0 0 16px}
  .interior .service-list{margin-top:12px;padding-left:8px}
  .interior .price-tag{left:426px;top:120px;width:158px;height:72px}

  .surcharge-note{
    position:absolute;left:642px;top:834px;color:var(--white);font-weight:700;
    font-size:25px;line-height:30px;text-transform:uppercase;
  }

  .engine{left:186px;top:1032px;width:598px;height:152px;background:var(--blue-panel);padding:8px 0 0 14px}
  .engine .service-list{margin-top:6px;padding-left:6px;font-size:21px}
  .engine .price-tag{left:426px;top:18px;width:158px;height:70px}
  .engine .headlight{
    margin-top:6px;font-family:"Archivo Black",sans-serif;color:var(--yellow);
    font-size:28px;line-height:32px;transform:skewX(-10deg);transform-origin:left bottom;
  }
  .engine .price-mini{
    position:absolute;left:478px;top:100px;width:106px;height:48px;
    background:var(--white);border:3px solid var(--red);color:var(--red);
    font-family:"Roboto",sans-serif;font-weight:700;font-size:31px;line-height:42px;text-align:center;letter-spacing:-.5px;
  }
</style>
</head>
<body>
<main class="flyer">
  <div class="water-texture" role="img" aria-label="Blue water background with droplets"></div>
  <div class="car-photo" role="img" aria-label="Photo of a shiny blue car front covered in water droplets"></div>

  <header class="brand">
    <h1 class="brand-name">Corvel's<br>Auto Detailing</h1>
    <div class="brand-phone">call 5047162283</div>
  </header>

  <section class="panel full">
    <h2 class="panel-title">Full Detail</h2>
    <ul class="service-list">
      <li>Wash car &amp; dry with microfiber towels</li>
      <li>Clean wheels &amp; wheel wells</li>
      <li>Clean all windows &amp; mirrors</li>
      <li>Vacuum carpets &amp; mats</li>
      <li>Wipe door jams</li>
      <li>Apply tire dressing</li>
      <li>Apply polish for shine &amp; to remove minor scratches</li>
      <li>Apply premium wax to protect the clear coat.</li>
      <li>Vacuum interior &amp; trunk</li>
      <li>Shampoo carpets, floor mats, seats</li>
      <li>Deep clean upholstery &amp; leather</li>
      <li>Apply conditioner to leather seats</li>
      <li>Clean all windows &amp; mirrors</li>
    </ul>
    <div class="price-tag"><span class="from">STARTING AT</span><span class="amount">$149.99</span><span class="tax">+ TAX</span></div>
  </section>

  <section class="panel exterior">
    <h2 class="panel-title">Exterior Detail</h2>
    <ul class="service-list">
      <li>Wash car &amp; dry with microfiber towels</li>
      <li>Clean wheels &amp; wheel wells</li>
      <li>Clean all windows &amp; mirrors</li>
      <li>Vacuum carpets &amp; mats</li>
      <li>Wipe door jams</li>
      <li>Apply tire dressing</li>
      <li>Apply polish for shine &amp; to remove minor scratches</li>
      <li>Apply premium wax to protect clear coat.</li>
    </ul>
    <div class="price-tag"><span class="from">STARTING AT</span><span class="amount">$59.99</span><span class="tax">+ TAX</span></div>
  </section>

  <section class="panel interior">
    <h2 class="panel-title">Interior Detail</h2>
    <ul class="service-list">
      <li>Wash car &amp; dry with microfiber towels</li>
      <li>Vacuum interior &amp; trunk</li>
      <li>Shampoo carpets, floor mats, seats</li>
      <li>Deep clean upholstery &amp; leather</li>
      <li>Apply conditioner to leather seats</li>
      <li>Clean all windows &amp; mirrors</li>
    </ul>
    <div class="price-tag"><span class="from">STARTING AT</span><span class="amount">$59.99</span><span class="tax">+ TAX</span></div>
  </section>

  <p class="surcharge-note">Additional<br>charges<br>apply<br>for<br>larger<br>vehicles</p>

  <section class="panel engine">
    <h2 class="panel-title">Engine Detail</h2>
    <ul class="service-list">
      <li>Degrease engine, apply dressing</li>
      <li>to engine, clean hood compartment</li>
    </ul>
    <div class="headlight">HEADLIGHT Restoration</div>
    <div class="price-tag"><span class="from">STARTING AT</span><span class="amount">$39.99</span><span class="tax">+ TAX</span></div>
    <div class="price-mini">$19.99</div>
  </section>
</main>
</body>
</html>
```